Sales Flyer

I am looking for a one page 8x11 flyer that I can print and mail to potential customers. I want to get the message across to potential customers that if they purchase a mobile patrol service with my company then I will provide them with a free camera system with installation or intrusion alarm system with install.

I don't photos to add to the flyer but I would like to to have a couple of security related photos. Can the designers obtain applicable photos?

```html
<!DOCTYPE html>
<html lang="en">
<head>
<meta charset="utf-8">
<title>Keystone Guard Group – Sales Flyer</title>
<link href="https://fonts.googleapis.com/css2?family=Bebas+Neue&family=Roboto+Condensed:wght@400;700&family=Roboto:wght@400;500&display=swap" rel="stylesheet">
<style>
  :root {
    --brand-blue: #1f8fd6;
    --brand-blue-deep: #0f5f9e;
    --brand-blue-light: #3fb2ee;
    --ink: #111417;
    --ink-soft: #4a4f55;
    --panel-dark: #1c1e21;
    --panel-mid: #2c2f33;
    --card-bg: #f1f2f3;
    --white: #ffffff;
    --silver: #b9bcc0;
  }
  * { box-sizing: border-box; margin: 0; padding: 0; }
  html, body { width: 1032px; height: 1200px; overflow: hidden; background: #ffffff; }
  .flyer {
    position: relative; width: 1032px; height: 1200px; overflow: hidden;
    background: var(--white);
    font-family: "Roboto Condensed", Arial, sans-serif;
  }

  /* Hero */
  .hero-photo {
    position: absolute; left: 0; top: 0; width: 1032px; height: 560px;
    background: linear-gradient(90deg, #ffffff 0%, #f3f5f7 25%, #c9d2da 55%, #aab6c1 100%);
  }
  .hero-fade {
    position: absolute; left: 0; top: 0; width: 1032px; height: 560px;
    background: linear-gradient(180deg, rgba(255,255,255,0.85) 0%, rgba(255,255,255,0) 40%, rgba(255,255,255,0) 80%, rgba(255,255,255,0.6) 100%);
  }
  .camera-photo {
    position: absolute; left: 590px; top: 0; width: 442px; height: 300px;
    border-radius: 0 0 0 150px;
    background: radial-gradient(ellipse at 50% 80%, #2b2d30 0%, #3c3f43 35%, #dfe1e3 60%, #f4f5f6 100%);
  }
  .brand {
    position: absolute; left: 62px; top: 60px;
    font-family: "Roboto Condensed", Arial, sans-serif; font-weight: 700;
    font-size: 44px; line-height: 46px; letter-spacing: 1px;
    color: var(--brand-blue-deep);
  }
  .headline {
    position: absolute; left: 56px; top: 218px;
    font-family: "Bebas Neue", Impact, sans-serif; font-size: 58px; line-height: 68px;
    color: var(--ink); letter-spacing: 0.5px;
  }
  .swoosh { position: absolute; left: 0; top: 430px; }

  .photo-circle {
    position: absolute; border-radius: 50%;
    border: 7px solid #d8dbde;
    box-shadow: 0 0 0 5px var(--brand-blue), 0 6px 14px rgba(0,0,0,0.35);
  }
  .photo-circle--cameras { left: 648px; top: 355px; width: 178px; height: 178px;
    background: radial-gradient(circle at 45% 45%, #e1a55a 0%, #9a5a23 45%, #2e1f14 100%); }
  .photo-circle--monitors { left: 810px; top: 328px; width: 210px; height: 210px;
    background: radial-gradient(circle at 50% 40%, #d99a50 0%, #6b4628 45%, #1b1a19 100%); }

  /* Left column */
  .offer {
    position: absolute; left: 42px; top: 582px; width: 520px;
    font-weight: 700; font-size: 20.5px; line-height: 27px; text-transform: uppercase; color: var(--ink);
  }
  .offer .accent { color: var(--brand-blue-deep); }

  .system-card {
    position: absolute; left: 40px; width: 516px; height: 194px;
    background: var(--card-bg);
    box-shadow: 0 3px 8px rgba(0,0,0,0.22);
    border-bottom: 10px solid var(--brand-blue);
  }
  .system-card--camera { top: 712px; }
  .system-card--alarm { top: 925px; }
  .system-card__ribbon {
    position: absolute; right: 0; top: 0; height: 48px; width: 318px;
    background: linear-gradient(90deg, var(--brand-blue-light), var(--brand-blue-deep));
    clip-path: polygon(12% 0, 100% 0, 100% 100%, 0 100%);
    color: var(--white); font-weight: 700; font-size: 24px; line-height: 48px;
    text-align: right; padding-right: 14px; text-transform: uppercase; white-space: nowrap;
  }
  .system-card__image {
    position: absolute; left: 30px; top: 32px; width: 180px; height: 130px;
    background: linear-gradient(180deg, #fafafa, #cfd2d5);
  }
  .system-card__text {
    position: absolute; left: 232px; top: 70px; width: 272px;
    font-family: "Roboto", Arial, sans-serif; font-size: 20px; line-height: 24px; color: var(--ink-soft);
  }

  .call-bar {
    position: absolute; left: 0; top: 1130px; width: 588px; height: 70px;
    background: linear-gradient(180deg, #3a3d41, #1d1f22);
    color: var(--white); display: flex; align-items: center; gap: 18px; padding-left: 48px;
    font-weight: 700; font-size: 30px; letter-spacing: 1px; white-space: nowrap;
  }
  .call-bar .number { font-weight: 400; letter-spacing: 2px; }

  /* Right panel */
  .why-panel {
    position: absolute; left: 594px; top: 560px; width: 438px; height: 640px;
    background:
      repeating-linear-gradient(45deg, rgba(255,255,255,0.03) 0 2px, transparent 2px 6px),
      linear-gradient(180deg, var(--panel-mid), var(--panel-dark));
  }
  .why-tab {
    position: absolute; left: 580px; top: 576px; width: 452px; height: 40px;
    background: linear-gradient(90deg, var(--brand-blue-light), var(--brand-blue-deep));
    border-radius: 10px 0 0 10px;
    color: var(--white); font-weight: 700; font-size: 21px; line-height: 40px;
    padding-left: 18px; text-transform: uppercase; white-space: nowrap; overflow: hidden;
  }
  .why-list {
    position: absolute; left: 612px; top: 640px; width: 396px; list-style: none;
    font-family: "Roboto", Arial, sans-serif; font-size: 16.5px; line-height: 20px; color: var(--white);
  }
  .why-list li { display: flex; gap: 10px; margin-bottom: 16px; }
  .why-list svg { flex: none; margin-top: 2px; }
  .why-cta {
    position: absolute; left: 612px; top: 904px; width: 400px; text-align: center;
    font-weight: 700; font-size: 21px; line-height: 24px; text-transform: uppercase; color: var(--brand-blue);
  }

  .contact-box {
    position: absolute; left: 586px; top: 992px; width: 446px; height: 208px;
    background: linear-gradient(135deg, #3cb6f0 0%, #1a86cf 55%, #0f5f9e 100%);
    border-radius: 10px 0 0 0;
    color: var(--white);
  }
  .contact-box h2 {
    position: absolute; left: 24px; top: 30px;
    font-weight: 400; font-size: 24px; text-transform: uppercase; letter-spacing: 0.5px;
  }
  .contact-list {
    position: absolute; left: 26px; top: 80px; list-style: none;
    font-family: "Roboto", Arial, sans-serif; font-weight: 500; font-size: 17px; line-height: 34px;
  }
  .contact-list li { display: flex; align-items: center; gap: 14px; white-space: nowrap; }
  .region-seal {
    position: absolute; left: 898px; top: 990px; width: 108px; height: 108px; border-radius: 50%;
    background: radial-gradient(circle at 40% 35%, #f2f3f4, var(--silver) 60%, #8a8d91);
    border: 3px dashed #e6e7e9;
    box-shadow: 0 3px 8px rgba(0,0,0,0.35);
    display: flex; align-items: center; justify-content: center; text-align: center;
    font-weight: 700; font-size: 14px; line-height: 15px; color: #2a2c2f; text-transform: uppercase;
  }
</style>
</head>
<body>
<main class="flyer">
  <div class="hero-photo" role="img" aria-label="Hazy city skyline photograph"></div>
  <div class="hero-fade"></div>
  <div class="camera-photo" role="img" aria-label="Photograph of a ceiling-mounted dome security camera"></div>

  <div class="brand">KEYSTONE GUARD<br>GROUP</div>

  <h1 class="headline">Does your business<br>currently use security guards<br>or mobile patrols?</h1>

  <svg class="swoosh" width="1032" height="130" viewBox="0 0 1032 130" aria-hidden="true">
    <path d="M0 0 L0 60 L308 125 L600 72 L600 52 L308 100 Z" fill="#ffffff"/>
    <path d="M0 18 Q140 62 308 108 L600 58 L600 66 L308 120 Q130 70 0 34 Z" fill="var(--brand-blue)"/>
    <path d="M0 40 L308 122 L600 70 L600 130 L0 130 Z" fill="#ffffff"/>
  </svg>

  <div class="photo-circle photo-circle--cameras" role="img" aria-label="Photograph of security cameras on a pole at dusk"></div>
  <div class="photo-circle photo-circle--monitors" role="img" aria-label="Photograph of a control room with surveillance monitors"></div>

  <p class="offer"><span class="accent">Partner with Keystone Guard Group</span> for your guard or mobile services and receive one of the following security systems with installation free of charge.</p>

  <section class="system-card system-card--camera">
    <div class="system-card__ribbon">Free Security Systems</div>
    <div class="system-card__image" role="img" aria-label="Product photo of a dome camera and network video recorder"></div>
    <p class="system-card__text">Lumora 6 high resolution security camera system with a 2TB NVR.</p>
  </section>

  <section class="system-card system-card--alarm">
    <div class="system-card__ribbon">Free Security Systems</div>
    <div class="system-card__image" role="img" aria-label="Product photo of an alarm keypad, sensors and key fob"></div>
    <p class="system-card__text">Sentrel intrusion alarm system with motion sensors, door contacts and glass break detectors.</p>
  </section>

  <div class="call-bar">
    <span>CALL US NOW</span>
    <svg width="30" height="30" viewBox="0 0 24 24" aria-hidden="true"><path d="M6.6 10.8a15 15 0 0 0 6.6 6.6l2.2-2.2a1 1 0 0 1 1-.25 11.4 11.4 0 0 0 3.6.57 1 1 0 0 1 1 1V20a1 1 0 0 1-1 1A17 17 0 0 1 3 4a1 1 0 0 1 1-1h3.5a1 1 0 0 1 1 1c0 1.25.2 2.450.57 3.57a1 1 0 0 1-.25 1z" fill="#fff"/></svg>
    <span class="number">780.555.0142</span>
  </div>

  <div class="why-panel"></div>
  <div class="why-tab">Why partner with Keystone Guard Group</div>

  <ul class="why-list">
    <li><svg width="16" height="16" viewBox="0 0 16 16" aria-hidden="true"><circle cx="8" cy="8" r="7.5" fill="#fff"/><path d="M4.5 8.2l2.3 2.2 4.7-4.8" stroke="#0f5f9e" stroke-width="1.8" fill="none"/></svg><span>We specialize in both security personnel and security system installations.</span></li>
    <li><svg width="16" height="16" viewBox="0 0 16 16" aria-hidden="true"><circle cx="8" cy="8" r="7.5" fill="#fff"/><path d="M4.5 8.2l2.3 2.2 4.7-4.8" stroke="#0f5f9e" stroke-width="1.8" fill="none"/></svg><span>All of our security guard and mobile patrol services come with access to our online reporting software. Contact us for a free demo to see how our software can help you.</span></li>
    <li><svg width="16" height="16" viewBox="0 0 16 16" aria-hidden="true"><circle cx="8" cy="8" r="7.5" fill="#fff"/><path d="M4.5 8.2l2.3 2.2 4.7-4.8" stroke="#0f5f9e" stroke-width="1.8" fill="none"/></svg><span>Our responsiveness to clients is unmatched.</span></li>
    <li><svg width="16" height="16" viewBox="0 0 16 16" aria-hidden="true"><circle cx="8" cy="8" r="7.5" fill="#fff"/><path d="M4.5 8.2l2.3 2.2 4.7-4.8" stroke="#0f5f9e" stroke-width="1.8" fill="none"/></svg><span>Our mobile service includes free alarm responses.</span></li>
  </ul>

  <p class="why-cta">Contact us today to discuss<br>how we can help you with your<br>security needs.</p>

  <section class="contact-box">
    <h2>Contact Us</h2>
    <ul class="contact-list">
      <li><svg width="16" height="16" viewBox="0 0 24 24" aria-hidden="true"><path d="M6.6 10.8a15 15 0 0 0 6.6 6.6l2.2-2.2a1 1 0 0 1 1-.25 11.4 11.4 0 0 0 3.6.57 1 1 0 0 1 1 1V20a1 1 0 0 1-1 1A17 17 0 0 1 3 4a1 1 0 0 1 1-1h3.5a1 1 0 0 1 1 1c0 1.25.2 2.45.57 3.57a1 1 0 0 1-.25 1z" fill="#fff"/></svg>780.555.0142</li>
      <li><svg width="16" height="16" viewBox="0 0 24 24" aria-hidden="true"><rect x="2" y="5" width="20" height="14" rx="2" fill="#fff"/><path d="M3 6l9 7 9-7" stroke="#1a86cf" stroke-width="2" fill="none"/></svg>sam@keystoneguardgroup.com</li>
      <li><svg width="16" height="16" viewBox="0 0 24 24" aria-hidden="true"><circle cx="12" cy="12" r="9.5" stroke="#fff" stroke-width="2" fill="none"/><ellipse cx="12" cy="12" rx="4" ry="9.5" stroke="#fff" stroke-width="2" fill="none"/><path d="M2.5 12h19" stroke="#fff" stroke-width="2"/></svg>KeystoneGuardGroup.com</li>
    </ul>
  </section>

  <div class="region-seal">Serving<br>all of<br>Alberta</div>
</main>
</body>
</html>
```